Stationery Design Needed: Business Card, Letterhead, Folder Design

Logo files attached I plan on using the standard us folder size 9x12 as well as standard US business card and letter head. I am the owner of Meadowfall Restorative Spine Clinic, www.meadowfallspineclinic.example. I now have two locations, each with the same phone number and website. I enclosed my slogan and the information. I practice in an honest, ethical manor and place patients at a top priority. I want the designs to fit with my logo which symbolizes a blend of the symbol for ethical, honesty ( the peacock ) and the medusa ( medicine ) . I want to use the colors form my website blue, grey, silver to blend in and be cohesive and also match along the modern but natural colors along with blue and grey from the office. I want my cards and stationary to stand out

Target Market(s)

Lawyers, Surgeons, Primary Care Physicians Chiropractors

Industry/Entity Type

Business

Contact Information for Business Card

I want the cards and folders to stand out ...Bold colors I like the dark blue the best as I want this to be my signature color ...See below
I don t want too much white or too much aqua blue

Colors
3277b5

Requirements
Must have
• On Business cards... Must have logo, My name and practice, Two addresses, and my certifications from anesthesia and pain medicine .... web site easy to read for my target age audience 40 +
Nice to have
• slogan and other certifications
Should not have
• Confusing small to real letters ... so may need double sides but with all important on the front

```html
<!DOCTYPE html>
<html lang="en">
<head>
<meta charset="utf-8">
<title>Meadowfall Restorative Spine Clinic – Stationery</title>
<link rel="stylesheet" href="https://fonts.googleapis.com/css2?family=Arimo:wght@400;700&family=Montserrat:wght@400;500;600;700&display=swap">
<style>
  :root{
    --stage:#8a8a8a;
    --navy:#253a58;
    --navy-text:#1f2f56;
    --blue:#1e90d6;
    --silver:#c9cacc;
    --frame:#d6d8dc;
    --paper:#ffffff;
    --ink:#111111;
    --label:#ffffff;
  }
  *{box-sizing:border-box;margin:0;padding:0}
  html,body{width:1200px;height:1200px;overflow:hidden;background:var(--stage)}
  .canvas{position:relative;width:1200px;height:1200px;font-family:"Montserrat",sans-serif}
  .piece-label{position:absolute;color:var(--label);font-family:"Arimo",sans-serif;font-weight:700;font-size:21px;transform:translateX(-50%);white-space:nowrap}
  .shadow{box-shadow:4px 5px 6px rgba(0,0,0,.45)}

  /* Letterhead */
  .letterhead{position:absolute;left:11px;top:72px;width:581px;height:770px;background:var(--paper)}
  .lh-brand{position:absolute;left:32px;top:34px;width:150px;text-align:center}
  .brand-mark{display:block;border-radius:50%;background:var(--blue);margin:0 auto}
  .lh-brand .brand-mark{width:80px;height:80px}
  .lh-brand .brand-name{margin-top:12px;color:var(--blue);font-weight:700;font-size:13px;line-height:1.2}
  .lh-contact{position:absolute;right:24px;top:48px;text-align:right;color:var(--navy-text);font-size:10.5px;font-weight:500;line-height:21px}
  .lh-contact b{font-weight:700}
  .lh-letter{position:absolute;left:32px;top:242px;width:531px;font-family:"Arimo",sans-serif;color:var(--ink)}
  .lh-salutation{font-weight:700;font-size:13px}
  .lh-body{margin-top:26px;font-size:13px;line-height:17.5px;text-align:justify;letter-spacing:.3px}
  .lh-signoff{margin-top:46px;font-size:13px;line-height:19px}
  .lh-signoff strong{display:block}

  /* Folder */
  .folder{position:absolute;left:602px;top:72px;width:582px;height:770px;background:var(--navy)}
  .folder-frame{position:absolute;inset:8px;border:3px solid var(--frame)}
  .folder .brand-mark{position:absolute;left:171px;top:190px;width:240px;height:240px}
  .folder-name{position:absolute;left:30px;right:30px;top:520px;text-align:center;color:var(--blue);font-weight:700;font-size:36px;line-height:44px}
  .folder-web{position:absolute;left:0;right:0;top:722px;text-align:center;color:var(--frame);font-weight:500;font-size:19px;letter-spacing:2.4px}

  /* Business card front */
  .card-front{position:absolute;left:97px;top:871px;width:413px;height:247px;background:var(--navy)}
  .card-front-frame{position:absolute;inset:12px 13px 12px 13px;border:1.5px solid var(--frame)}
  .card-front .brand-mark{position:absolute;left:157px;top:26px;width:100px;height:100px}
  .cert-title{position:absolute;left:0;right:0;top:189px;text-align:center;color:var(--frame);font-size:10px;font-weight:500}
  .cert-title span{border-bottom:1px solid var(--frame);padding-bottom:1px}
  .cert-list{position:absolute;left:0;right:0;top:208px;text-align:center;color:var(--frame);font-size:10px;line-height:14px;letter-spacing:.3px}

  /* Business card back */
  .card-back{position:absolute;left:692px;top:871px;width:414px;height:247px;background:var(--silver)}
  .cb-brand{position:absolute;left:12px;top:14px;width:180px;text-align:center}
  .cb-brand .brand-mark{width:110px;height:110px}
  .cb-brand .brand-name{margin-top:14px;color:var(--blue);font-weight:700;font-size:14px;line-height:1.2}
  .cb-details{position:absolute;right:26px;top:30px;text-align:right;color:var(--navy-text)}
  .cb-name{font-size:14px;font-weight:600;line-height:16px}
  .cb-primary{margin-top:14px;font-size:11px;font-weight:600;line-height:15.5px}
  .cb-secondary{margin-top:14px;font-size:11px;line-height:15.5px}
  .cb-phones{margin-top:14px;font-size:11px;line-height:19px}
  .cb-phones b{font-weight:700}
  .cb-band{position:absolute;left:0;right:0;bottom:0;height:33px;background:var(--navy);color:#fff;text-align:center;font-size:11px;font-weight:500;line-height:33px;letter-spacing:.3px}
</style>
</head>
<body>
<main class="canvas">

  <div class="piece-label" style="left:302px;top:35px">Letterhead A4</div>
  <div class="piece-label" style="left:898px;top:35px">Folder 9 X 12</div>

  <section class="letterhead shadow">
    <div class="lh-brand">
      <span class="brand-mark"></span>
      <div class="brand-name">Meadowfall Restorative Spine Clinic</div>
    </div>
    <address class="lh-contact" style="font-style:normal">
      <div><b>PH :</b> 555-014-7721</div>
      <div><b>F :</b> 555-014-7722</div>
      <div><b>www.meadowfallspineclinic.example</b></div>
      <div><b>4810 Larkspur Ave Fairbrook,</b></div>
      <div style="line-height:20px"><b>N.J. 07999</b></div>
    </address>
    <article class="lh-letter">
      <p class="lh-salutation">Dear Mr.Owen Hartley</p>
      <p class="lh-body">Logo files attached I plan on using the standard us folder size 9x12 as well as standard US business card and letter head. I am the owner of Meadowfall Restorative Spine Clinic, www.meadowfallspineclinic.example. I now have two locations, each with the same phone number and website. I enclosed my slogan and the information. I practice in an honest, ethical manor and place patients at a top priority. I want the designs to fit with my logo which symbolizes a blend of the symbol for ethical, honesty ( the peacock ) and the medusa ( medicine ) . I want to use the colors form my website blue, grey, silver to blend in and be cohesive and also match along the modern but natural colors along with blue and grey from the office. I want my cards and stationary to stand out Thank you.</p>
      <p class="lh-signoff"><strong>Rowan Vale</strong>Graphic Designer</p>
    </article>
  </section>

  <section class="folder shadow">
    <div class="folder-frame"></div>
    <span class="brand-mark"></span>
    <div class="folder-name">Meadowfall Restorative Spine Clinic</div>
    <div class="folder-web">www.meadowfallspineclinic.example</div>
  </section>

  <section class="card-front shadow">
    <div class="card-front-frame"></div>
    <span class="brand-mark"></span>
    <div class="cert-title"><span>BOARD CERTIFICATIONS</span></div>
    <div class="cert-list">Certified by the Northfield Board of Pain Medicine<br>Certified by the Northfield Board of Anesthesiology</div>
  </section>

  <section class="card-back shadow">
    <div class="cb-brand">
      <span class="brand-mark"></span>
      <div class="brand-name">Meadowfall Restorative Spine Clinic</div>
    </div>
    <div class="cb-details">
      <div class="cb-name">Owen R. Hartley,<br>D.O.</div>
      <div class="cb-primary">4810 Larkspur Ave<br>Fairbrook, N.J. 07999</div>
      <div class="cb-secondary">2205 Orchard Rd, Suite 118<br>Millbrook, N.J. 07998-1120</div>
      <div class="cb-phones"><b>Ph :</b> 555-014-7721<br><b>Fax :</b> 555-014-7722</div>
    </div>
    <div class="cb-band">www.meadowfallspineclinic.example</div>
  </section>

  <div class="piece-label" style="left:302px;top:1132px">Front Side</div>
  <div class="piece-label" style="left:898px;top:1132px">Back Side</div>

</main>
</body>
</html>
```